Zielgruppe
Wir sind eine Weiterbildungsfirma mit der Zielgruppe Unternehmer, Selbstständige, Führungskräfte und Vertriebler.
Aufgabenstellung
Es soll dynamisch, elegant und professionell wirken. Der Titel muss gut lesbar sein.
(Wir haben einen Pixmora-Foto-Account auf Abo-Basis.)
Der Titel lautet neu: Die Kelbing-Prinzipien für echte Durchbrüche

```html
<!DOCTYPE html>
<html lang="de">
<head>
<meta charset="utf-8">
<title>Die Kelbing-Prinzipien für echte Durchbrüche – Buchcover</title>
<link rel="stylesheet" href="https://fonts.googleapis.com/css2?family=Bebas+Neue&family=Jost:wght@500;600&display=swap">
<style>
  :root {
    --backdrop: #c3c3c3;
    --paper: #f3f3f3;
    --paper-fringe: #e6e6e6;
    --navy-light: #2c3a8c;
    --navy: #27287a;
    --navy-dark: #231d5c;
    --gold: #d8a92a;
    --gold-deep: #d4a62a;
    --ink: #1a1a2a;
    --subtitle: #2b3494;
    --white: #ffffff;
  }
  html, body {
    margin: 0;
    padding: 0;
    width: 1195px;
    height: 1200px;
    overflow: hidden;
    background: var(--backdrop);
  }
  .book-cover {
    position: absolute;
    left: 207px;
    top: 15px;
    width: 780px;
    height: 1170px;
    background: var(--paper);
    overflow: hidden;
  }
  .author {
    position: absolute;
    top: 58px;
    left: 0;
    width: 100%;
    text-align: center;
    font-family: "Jost", sans-serif;
    font-weight: 600;
    font-size: 52px;
    letter-spacing: 0.13em;
    color: var(--gold);
    margin: 0;
    line-height: 64px;
  }
  .cover-art {
    position: absolute;
    left: 0;
    top: 0;
    width: 780px;
    height: 1170px;
  }
  .title-line {
    font-family: "Bebas Neue", sans-serif;
  }
  .badge-text {
    font-family: "Bebas Neue", sans-serif;
    font-size: 31px;
  }
  .subtitle {
    position: absolute;
    top: 996px;
    left: 60px;
    width: 660px;
    margin: 0;
    text-align: center;
    font-family: "Jost", sans-serif;
    font-weight: 500;
    font-size: 26.5px;
    line-height: 34.5px;
    letter-spacing: 0.02em;
    color: var(--subtitle);
  }
</style>
</head>
<body>
<main class="book-cover">
  <svg class="cover-art" viewBox="0 0 780 1170" xmlns="http://www.w3.org/2000/svg">
    <defs>
      <linearGradient id="band-fill" x1="0" y1="0" x2="1" y2="0">
        <stop offset="0" stop-color="#3a4a9a"/>
        <stop offset="0.05" stop-color="var(--navy-light)"/>
        <stop offset="0.5" stop-color="var(--navy)"/>
        <stop offset="1" stop-color="var(--navy-dark)"/>
      </linearGradient>
      <linearGradient id="title-gold" x1="100" y1="420" x2="700" y2="750" gradientUnits="userSpaceOnUse">
        <stop offset="0" stop-color="#e2b94a"/>
        <stop offset="0.2" stop-color="#fffdf4"/>
        <stop offset="0.35" stop-color="#f3e4b0"/>
        <stop offset="0.55" stop-color="#fdfbe6"/>
        <stop offset="0.78" stop-color="#e8dc4c"/>
        <stop offset="1" stop-color="#c4a84a"/>
      </linearGradient>
    </defs>

    <!-- upper torn paper fringe -->
    <path fill="var(--paper-fringe)" d="M0 178 L30 172 L62 180 L95 170 L130 177 L170 168 L205 176 L240 171 L280 179 L320 169 L360 176 L400 170 L440 178 L480 168 L520 177 L560 171 L600 179 L640 169 L680 176 L720 170 L750 177 L780 172 L780 220 L0 220 Z"/>
    <!-- blue title band -->
    <path fill="url(#band-fill)" d="M0 207 L25 203 L55 208 L85 202 L120 206 L150 212 L185 214 L215 209 L250 216 L285 211 L320 218 L355 213 L390 217 L420 210 L455 214 L490 208 L525 212 L560 207 L600 211 L640 205 L680 209 L720 204 L750 208 L780 205
      L780 925 L750 922 L715 927 L680 921 L645 926 L610 920 L575 925 L540 919 L505 924 L470 918 L435 923 L400 917 L365 922 L330 916 L295 921 L260 915 L225 920 L190 914 L155 918 L120 912 L85 917 L50 910 L20 915 L0 911 Z"/>
    <!-- lower torn paper fringe -->
    <path fill="var(--paper-fringe)" opacity="0.7" d="M0 915 L20 919 L50 914 L85 921 L120 916 L155 922 L190 918 L225 924 L260 919 L295 925 L330 920 L365 926 L400 921 L435 927 L470 922 L505 928 L540 923 L575 929 L610 924 L645 930 L680 925 L715 931 L750 926 L780 929 L780 945 L0 945 Z"/>

    <!-- title -->
    <text class="title-line" x="390" y="378" text-anchor="middle" font-size="94" fill="var(--white)">DIE</text>
    <text class="title-line" x="100" y="580" font-size="232" textLength="593" lengthAdjust="spacingAndGlyphs" fill="url(#title-gold)">KELBING-</text>
    <text class="title-line" x="100" y="744" font-size="196" textLength="593" lengthAdjust="spacingAndGlyphs" fill="url(#title-gold)">PRINZIPIEN</text>
    <text class="title-line" x="100" y="830" font-size="92" textLength="593" lengthAdjust="spacingAndGlyphs" fill="var(--white)">FÜR ECHTE DURCHBRÜCHE</text>

    <!-- free audiobook seal -->
    <g class="seal" transform="translate(630 262)">
      <g fill="var(--gold-deep)">
        <rect x="-75" y="-75" width="150" height="150" transform="rotate(0)"/>
        <rect x="-75" y="-75" width="150" height="150" transform="rotate(9)"/>
        <rect x="-75" y="-75" width="150" height="150" transform="rotate(18)"/>
        <rect x="-75" y="-75" width="150" height="150" transform="rotate(27)"/>
        <rect x="-75" y="-75" width="150" height="150" transform="rotate(36)"/>
        <rect x="-75" y="-75" width="150" height="150" transform="rotate(45)"/>
        <rect x="-75" y="-75" width="150" height="150" transform="rotate(54)"/>
        <rect x="-75" y="-75" width="150" height="150" transform="rotate(63)"/>
        <rect x="-75" y="-75" width="150" height="150" transform="rotate(72)"/>
        <rect x="-75" y="-75" width="150" height="150" transform="rotate(81)"/>
      </g>
      <g transform="rotate(20)" text-anchor="middle">
        <text class="badge-text" x="0" y="-44" fill="var(--ink)">GRATIS DAZU:</text>
        <text class="badge-text" x="0" y="-14" fill="var(--navy)">DIE HÖRBUCH-</text>
        <text class="badge-text" x="0" y="16" fill="var(--navy)">AUSGABE</text>
        <text class="badge-text" x="0" y="44" font-size="27" fill="var(--navy)">ALS MP3</text>
      </g>
    </g>
  </svg>

  <h2 class="author">JONAS M. KELBING</h2>

  <p class="subtitle">Für das Lesen dieses Buches brauchen Sie<br>nur etwa zwei Stunden – oder an zwölf<br>Tagen jeweils zehn Minuten.</p>
</main>
</body>
</html>
```